New audiology website PSD design only - guaranteed

We need a clean and attractive website to replace an existing Audiology (hearing technology) website which will be wordpress based.
The current website is: http://pelmorahearing.com.au
They have a new logo and colors which you can find at www.quodel.net/temp/plh2018.pdf
We will no longer have a web shop in the new website
To enter the competition, we only need a sample of the home page.
The winning design will be asked to produce 2 standard page template alternatives as well (based on the winning home page design, but for a standard page layout)
The winning design must provide any photos used
We want a clean, credible site but with some warmth
Target Market(s)
All ages but needs to include the elderly
Industry/Entity Type
Medical And Science
Number of Pages Required
3 page
Look and feel
Each slider illustrates characteristics of the customer's brand and the style your logo design should communicate.

```html
<!DOCTYPE html>
<html lang="en">
<head>
<meta charset="utf-8">
<title>Pelmora Hearing</title>
<link rel="stylesheet" href="https://fonts.googleapis.com/css2?family=Poppins:ital,wght@0,400;0,500;0,600;0,700;1,400&family=Oswald:wght@500;600&family=Roboto+Condensed:ital,wght@0,400;1,400&display=swap">
<style>
:root{
  --orange:#f47a2a;
  --orange-dark:#e8691c;
  --ink:#2b2b2b;
  --text:#777;
  --muted:#999;
  --footer:#1c1c1c;
  --footer-text:#c9c9c9;
  --white:#fff;
  --tile-orange:#f4792b;
  --tile-blue:#3bb0f4;
  --tile-green:#3fcf5c;
  --tile-teal:#5fd0c6;
  --tile-coral:#ee6453;
  --tile-purple:#a867e0;
}
*{box-sizing:border-box;margin:0;padding:0}
html,body{width:699px;height:1200px;overflow:hidden;background:#fff}
body{font-family:"Poppins",sans-serif;color:var(--text)}
.page{position:relative;width:699px;height:1200px;overflow:hidden}
.abs{position:absolute}

/* header */
.hero{position:absolute;left:0;top:0;width:699px;height:350px;
  background:linear-gradient(100deg,#f4f5f6 0%,#e9ecef 40%,#c9ced4 62%,#8d96a2 80%,#b5bcc5 100%)}
.brand{position:absolute;left:79px;top:26px;display:flex;align-items:center;gap:6px;
  font-size:15px;font-weight:500;color:#555}
.brand-dot{width:20px;height:20px;border-radius:50%;border:2px solid var(--orange)}
.nav{position:absolute;left:279px;top:35px;display:flex;gap:11px;font-size:5.6px;font-weight:600;color:var(--ink);letter-spacing:.1px}
.nav .active{color:var(--orange);border-bottom:1px solid var(--orange);padding-bottom:3px}
.call-btn{position:absolute;left:530px;top:10px;width:91px;height:16px;border-radius:8px;
  background:var(--orange);color:#fff;font-size:6.5px;font-weight:600;text-align:center;line-height:16px}
.hero-title{position:absolute;left:84px;top:134px;font-family:"Oswald",sans-serif;font-weight:600;font-size:20px;color:var(--ink);letter-spacing:.2px}
.hero-title span{color:var(--orange)}
.hero-sub{position:absolute;left:84px;top:165px;font-family:"Roboto Condensed",sans-serif;font-style:italic;font-size:9.5px;color:#333}
.hero-copy{position:absolute;left:84px;top:184px;width:225px;font-size:5.4px;font-style:italic;line-height:10.5px;color:#333}
.btn{position:absolute;height:17px;border-radius:9px;font-size:5.6px;font-weight:600;font-style:italic;color:#fff;text-align:center;line-height:17px}
.btn-dark{left:83px;top:229px;width:72px;background:#4a4a4a}
.btn-orange{left:161px;top:229px;width:82px;background:var(--orange)}
.dots{position:absolute;left:93px;top:262px;display:flex;gap:8px}
.dots i{width:4px;height:4px;border-radius:50%;background:#444}
.dots i:first-child{background:var(--orange)}

/* services */
.tile{position:absolute;width:80px;height:58px;color:#fff;font-size:4.6px;font-weight:600;text-align:center}
.tile svg{position:absolute;left:28px;top:9px}
.tile b{position:absolute;left:0;right:0;bottom:7px;font-weight:600}
.section-title{font-size:8.5px;font-weight:700;color:var(--ink)}
.section-sub{font-size:4.8px;color:var(--muted);margin-top:3px}
.body-copy{font-size:5.6px;line-height:11px;color:var(--text)}
.services-info{position:absolute;left:377px;top:373px;width:240px}
.services-info .body-copy{margin-top:8px}
.outline-btn{position:absolute;left:379px;top:470px;width:115px;height:20px;border:1px solid #ddd;border-radius:10px;
  font-size:4.8px;font-weight:600;color:var(--ink);line-height:18px;padding-left:11px}
.outline-btn em{color:var(--orange);font-style:normal;font-size:8px;position:absolute;right:12px;top:0}

/* about */
.about{position:absolute;left:0;top:531px;width:699px;height:209px;background:#f6f6f6;border-top:1px solid #e8e8e8}
.about-photo{position:absolute;right:0;top:0;width:300px;height:209px;
  background:radial-gradient(ellipse at 62% 50%,#d9dadc 0%,#e6e2df 35%,#efedec 60%,#f6f6f6 85%)}
.about-text{position:absolute;left:80px;top:22px;width:340px}
.about-text .section-sub{color:var(--ink);margin-top:4px}
.about-text p{margin-top:7px}
.orange{color:var(--orange)}

/* doctors */
.doctors-photo{position:absolute;left:0;top:740px;width:322px;height:235px;
  background:linear-gradient(90deg,#8c6f5e 0%,#c9a895 30%,#e3cfc2 55%,#b6c8dc 80%,#dbe5ef 100%)}
.doctors-info{position:absolute;left:338px;top:766px;width:282px}
.doctors-info .section-sub{color:#777;font-size:4.8px}
.doctors-info .body-copy{margin-top:7px}
.doc{position:absolute;top:852px;width:57px;text-align:center}
.doc-photo{width:57px;height:50px;border:2px solid #e4e4e4;background:linear-gradient(180deg,#dfe6ec,#b9c3cc)}
.doc-name{font-size:4.8px;color:var(--ink);margin-top:7px}
.doc-role{font-size:3.7px;color:#777;margin-top:1px}
.next{position:absolute;left:558px;top:873px;width:10px;height:10px;border:1px solid #ccc;border-radius:50%;font-size:6px;line-height:8px;text-align:center;color:#bbb}
.doc-btn{position:absolute;left:346px;top:939px;width:67px;height:16px;background:var(--orange);color:#fff;font-size:5.2px;line-height:16px;text-align:center}

/* contact band */
.contact-band{position:absolute;left:0;top:975px;width:699px;height:74px;background:var(--orange);color:#fff}
.contact-item{position:absolute;top:24px;display:flex;gap:10px}
.contact-item h4{font-size:5.8px;font-weight:600}
.contact-item p{font-size:5.6px;margin-top:3px}
.contact-item small{display:block;font-size:4.8px;font-style:italic;margin-top:1px}
.newsletter-line{position:absolute;left:474px;top:1022px;width:143px;border-bottom:1px solid rgba(255,255,255,.6);font-size:4.2px;font-style:italic;padding-bottom:2px;color:#fff}

/* footer */
.footer{position:absolute;left:0;top:1049px;width:699px;height:151px;background:var(--footer);color:var(--footer-text)}
.f-col{position:absolute;top:20px;font-size:5.4px;line-height:12px}
.f-col h5{font-size:5.8px;font-weight:600;color:var(--orange);margin-bottom:8px}
.f-col h6{font-size:5.6px;font-weight:600;color:var(--orange)}
.f-col .closed{color:var(--orange);font-style:italic}
.f-rule{position:absolute;left:0;right:0;top:114px;border-top:1px solid #333}
.copyright{position:absolute;left:80px;top:128px;font-size:3.8px;color:#888}
.social{position:absolute;left:556px;top:125px;display:flex;gap:8px}
.social i{width:10px;height:10px;border-radius:50%}
</style>
</head>
<body>
<div class="page">

  <section class="hero" role="img" aria-label="Audiologist at a laptop running a hearing test while a patient wearing headphones sits in a glass booth"></section>
  <div class="brand"><span class="brand-dot"></span>Pelmora Hearing</div>
  <nav class="nav">
    <span class="active">HOME</span><span>YOUR HEARING</span><span>MUSICIANS</span><span>DOCTORS INFORMATION</span><span>ABOUT US</span><span>PRODUCTS</span><span>CONTACT US</span>
  </nav>
  <div class="call-btn">CALL : (02) 5550 1840</div>
  <h1 class="hero-title"><span>ENJOY THE SOUNDS</span> OF THE LIFE..!</h1>
  <p class="hero-sub">Find out what better hearing can mean for you..</p>
  <p class="hero-copy">Lorem ipsum dolor sit amet, consectetuer adipiscing elit. Aenean commodo ligula eget dolor. Aenean massa. Cum sociis natoque penatibus et magnis dis parturient montes, nascetur ridiculus mus. Donec quam</p>
  <div class="btn btn-dark">More Details</div>
  <div class="btn btn-orange">Book An Appointment</div>
  <div class="dots"><i></i><i></i><i></i><i></i></div>

  <div class="tile" style="left:77px;top:373px;background:var(--tile-orange)">
    <svg width="24" height="24" viewBox="0 0 24 24" fill="none" stroke="#fff" stroke-width="1.6"><path d="M8 14c0-6 3-9 6-9s5 3 5 6-3 4-3 7-2 4-4 4"/><path d="M4 4a14 14 0 0 1 4-3"/></svg>
    <b>PURE TONE AUDIOLOGY</b></div>
  <div class="tile" style="left:177px;top:373px;background:var(--tile-blue)">
    <svg width="24" height="24" viewBox="0 0 24 24" fill="none" stroke="#fff" stroke-width="1.4"><path d="M6 22v-5c-3-2-3-6-2-9s4-5 7-5 5 3 5 6l2 3h-2v3h-3v7"/><path d="M19 9v6M21 10v4"/></svg>
    <b>SPEECH TESTING</b></div>
  <div class="tile" style="left:279px;top:373px;background:var(--tile-green)">
    <svg width="24" height="24" viewBox="0 0 24 24" fill="none" stroke="#fff" stroke-width="1.4"><circle cx="12" cy="10" r="7"/><rect x="9" y="8" width="6" height="13"/></svg>
    <b>TYMPANOMETRY</b></div>
  <div class="tile" style="left:77px;top:443px;background:var(--tile-teal)">
    <svg width="24" height="24" viewBox="0 0 24 24" fill="none" stroke="#fff" stroke-width="1.6"><path d="M4 16v-4a8 8 0 0 1 16 0v4"/><rect x="3" y="14" width="4" height="7" rx="1"/><rect x="17" y="14" width="4" height="7" rx="1"/></svg>
    <b>PAEDIATRIC HEARING TEST</b></div>
  <div class="tile" style="left:177px;top:443px;background:var(--tile-coral)">
    <svg width="24" height="24" viewBox="0 0 24 24" fill="none" stroke="#fff" stroke-width="1.6"><ellipse cx="12" cy="10" rx="9" ry="7"/><path d="M12 3v14M12 17v5"/></svg>
    <b>AUDITORY BRAINSTEM</b></div>
  <div class="tile" style="left:279px;top:443px;background:var(--tile-purple)">
    <svg width="24" height="24" viewBox="0 0 24 24" fill="none" stroke="#fff" stroke-width="1.6"><rect x="3" y="8" width="18" height="7" rx="2"/><path d="M8 15v7M16 15v7M8 8V3h8v5"/></svg>
    <b>VIDEONYSTAGMOGRAPHY</b></div>

  <div class="services-info">
    <h2 class="section-title">OUR SERVICES</h2>
    <p class="section-sub">Our Departments &amp; Special Services</p>
    <p class="body-copy">Pelmora Hearing is a leading Hearing and Balance Clinic located in the inner suburbs of Sydney. Each of our custom built clinics have the most up to date diagnostic equipment available. We offer an extensive range of diagnostics conducted by highly experienced and fully trained Audiologists. We work closely with medical professionals to deliver outstanding and reliable services.</p>
  </div>
  <div class="outline-btn">ALL DEPARTMENTS &amp; SERVICES <em>→</em></div>

  <section class="about">
    <div class="about-photo" role="img" aria-label="Fingers holding a small behind-the-ear hearing aid"></div>
    <div class="about-text">
      <h2 class="section-title">WE'R THE BEST IN <span class="orange">MODERN AUDIOLOGY</span></h2>
      <p class="section-sub">We Provide Most Professional service since 1950</p>
      <p class="body-copy">Pelmora Hearing is an independently owned and managed professional audiology clinic. Our Audiologists are health-care professionals specialising in diagnosing, treating and monitoring everything to do with hearing and balance. At Pelmora Hearing we work closely with Ear, Nose and Throat specialists to ensure you receive the highest standards of medical care.</p>
      <p class="body-copy">Pelmora Hearing are state of the art hearing and balance clinics. We provide all brands of digital hearing aids, cochlear implants and assisted listening devices. We are diagnostic clinics, offering hearing tests for adults and children, balance tests, tinnitus testing and treatment, and auditory processing tests (APD).</p>
      <p class="body-copy">At Pelmora Hearing we are committed to excellence, we are at the forefront of providing detailed testing and treatment options. Our state-of-the-art clinics are purpose built, and our fully accredited Audiology team are experienced and at the top of their profession. Our success is measured by your satisfaction.</p>
    </div>
  </section>

  <div class="doctors-photo" role="img" aria-label="Doctor examining a young boy's ear with an otoscope"></div>
  <div class="doctors-info">
    <h2 class="section-title">OUR <span class="orange">DOCTORS</span></h2>
    <p class="section-sub">For appointments please phone <span class="orange">5550 1840</span></p>
    <p class="body-copy">Pelmora Hearing is one of Sydney's leading diagnostic hearing and balance clinics. Referring doctors can be assured that all testing and rehabilitation is reviewed to the highest industry standards. Our Audiologists also work closely with referring ENT's and Doctors to ensure all testing meets the needs of their practice.</p>
  </div>
  <div class="doc" style="left:342px"><div class="doc-photo" role="img" aria-label="Portrait of a doctor"></div><p class="doc-name">DANIEL PRICE</p><p class="doc-role">Tympanometry Specilist</p></div>
  <div class="doc" style="left:418px"><div class="doc-photo" role="img" aria-label="Portrait of a doctor"></div><p class="doc-name">LEENA MARSH</p><p class="doc-role">Tympanometry Specilist</p></div>
  <div class="doc" style="left:490px"><div class="doc-photo" role="img" aria-label="Portrait of a doctor"></div><p class="doc-name">OWEN HART</p><p class="doc-role">Tympanometry Specilist</p></div>
  <div class="next">›</div>
  <div class="doc-btn">View all Doctors &nbsp;›</div>

  <section class="contact-band">
    <div class="contact-item" style="left:82px">
      <svg width="28" height="24" viewBox="0 0 28 24" fill="none" stroke="#fff" stroke-width="1.3"><rect x="1" y="3" width="6" height="20" rx="2"/><rect x="8" y="5" width="19" height="18" rx="2"/><rect x="11" y="7" width="13" height="4"/><path d="M12 14h2M17 14h2M22 14h1M12 18h2M17 18h2M22 18h1"/></svg>
      <div><h4>CALL US</h4><p>(02) 5550 1840</p><small>Customer support troll free</small></div>
    </div>
    <div class="contact-item" style="left:267px">
      <svg width="24" height="24" viewBox="0 0 24 24" fill="none" stroke="#fff" stroke-width="1.3"><path d="M2 10l10-8 10 8v12H2z"/><path d="M2 10l10 7 10-7"/><path d="M6 12V5h12v7"/></svg>
      <div><h4>EMAIL US</h4><p>support@pelmorahearing.com.au</p><small>Normally Respond in 5-6 Hours</small></div>
    </div>
    <div class="contact-item" style="left:437px">
      <svg width="26" height="24" viewBox="0 0 26 24" fill="none" stroke="#fff" stroke-width="1.3"><rect x="3" y="5" width="20" height="14" rx="1"/><path d="M1 19h24M3 5l10 7 10-7"/></svg>
      <div><h4>SIGN UP FOR OUR NEWSLETTER</h4></div>
    </div>
  </section>
  <div class="newsletter-line">Your E-Mail address</div>

  <footer class="footer">
    <div class="f-col" style="left:82px">
      <h5>OUR LOCATIONS</h5>
      <h6>Kelverton</h6>
      Level 1, Suite 4,<br>18 Marlow Avenue,<br>Kelverton, NSW, 2061<br>Phone: 5550 1840
    </div>
    <div class="f-col" style="left:216px;top:40px">
      <h6>Ashbrook</h6>
      Shop 2, 40 Wattle Street<br>Ashbrook,<br>NSW, 2048<br>Phone : 5550 2613
    </div>
    <div class="f-col" style="left:367px">
      <h5>WORKING HOURS</h5>
      Monday - Friday<br><i>08.00 am - 10.00 pm</i><br>Saturday &amp; Sunday<br><span class="closed">Closed</span>
    </div>
    <div class="f-col" style="left:504px;line-height:11px">
      <h5>NAVIGATION</h5>
      Home<br>Your Hearing<br>Musicians<br>Doctors Information<br>About us<br>Contact us
    </div>
    <div class="f-rule"></div>
    <p class="copyright">© Pelmora Hearing 2018. All rights Reserved Terms and Conditions</p>
    <div class="social"><i style="background:#3b5a9a"></i><i style="background:#2aa3ef"></i><i style="background:#e0483b"></i><i style="background:#1a7bb6"></i></div>
  </footer>

</div>
</body>
</html>
```